Criação de Papelaria Profissional para Advocacia e Direito
A empresa queria:
" Ribeiro Tavares Advogados é um escritório boutique de atuação diversificada (full service) "

```html
<!DOCTYPE html>
<html lang="pt-BR">
<head>
<meta charset="utf-8">
<title>Ribeiro Tavares Advogados — Papelaria</title>
<link rel="stylesheet" href="https://fonts.googleapis.com/css2?family=Questrial&family=Cinzel:wght@400&display=swap">
<style>
  :root {
    --backdrop: #e6e7e9;
    --navy-deep: #18324a;
    --navy: #254a68;
    --navy-light: #3a6485;
    --paper: #f4f5f7;
    --paper-shade: #e3e5e8;
    --silver: #c9ced4;
    --ink: #1f3b55;
    --ink-soft: #6b7a88;
    --white: #ffffff;
  }
  * { box-sizing: border-box; margin: 0; padding: 0; }
  html, body { width: 1200px; height: 1200px; overflow: hidden; }
  body {
    background: var(--backdrop);
    font-family: "Questrial", sans-serif;
    position: relative;
  }

  /* ---------- Letterhead ---------- */
  .letterhead {
    position: absolute;
    left: 110px; top: 230px;
    width: 470px; height: 700px;
    background: linear-gradient(180deg, var(--white) 0%, var(--paper) 60%, var(--paper-shade) 100%);
    box-shadow: 0 10px 30px rgba(0,0,0,.15);
    overflow: hidden;
  }
  .letterhead__band { position: absolute; left: 0; top: 0; width: 100%; height: 110px; }
  .letterhead__mark {
    position: absolute; top: 24px; left: 0; width: 100%;
    display: flex; justify-content: center; align-items: center; gap: 8px;
    color: var(--white); font-size: 15px; letter-spacing: 2px;
  }
  .mark-square { width: 12px; height: 12px; border: 1.5px solid currentColor; }
  .letterhead__watermark {
    position: absolute; left: 28px; top: 400px;
    width: 300px; height: 170px;
    background: linear-gradient(135deg, rgba(255,255,255,.9), rgba(210,214,220,.5));
    border: 1px solid rgba(255,255,255,.8);
  }
  .letterhead__footer {
    position: absolute; left: 0; bottom: 22px; width: 100%;
    text-align: center; color: var(--ink);
  }
  .brand-name { font-size: 22px; letter-spacing: 2px; text-transform: uppercase; }
  .brand-sub {
    font-family: "Cinzel", serif; font-size: 8px; letter-spacing: 1.5px;
    color: var(--ink-soft); margin-top: 3px;
  }
  .brand-row { display: flex; justify-content: center; align-items: center; gap: 8px; }
  .contact-row {
    margin-top: 14px; display: flex; justify-content: center; gap: 20px;
    font-size: 7.5px; color: var(--ink-soft); line-height: 1.35;
  }
  .contact-item { display: flex; align-items: center; gap: 5px; text-align: left; }
  .contact-icon {
    width: 11px; height: 11px; border-radius: 50%;
    border: 1px solid var(--ink-soft); flex-shrink: 0;
  }

  /* ---------- Folder ---------- */
  .folder {
    position: absolute;
    left: 620px; top: 230px;
    width: 470px; height: 700px;
    background: radial-gradient(ellipse at 50% 25%, var(--navy-light) 0%, var(--navy) 45%, var(--navy-deep) 100%);
    box-shadow: 0 10px 30px rgba(0,0,0,.2);
    overflow: hidden;
  }
  .folder__brand {
    position: absolute; top: 200px; left: 0; width: 100%;
    text-align: center; color: var(--white);
  }
  .folder__brand .brand-name { font-size: 30px; letter-spacing: 3px; }
  .folder__brand .brand-sub { color: #c8d3de; font-size: 9px; margin-top: 6px; }
  .folder__watermark {
    position: absolute; left: 0; top: 370px;
    width: 340px; height: 200px;
    background: rgba(255,255,255,.05);
    border: 1px solid rgba(255,255,255,.08);
  }
  .folder__stripe {
    position: absolute; left: 0; bottom: 40px; width: 100%; height: 10px;
    background: linear-gradient(180deg, #eef1f4, var(--silver) 60%, #8b96a2);
  }
</style>
</head>
<body>
  <section class="letterhead">
    <svg class="letterhead__band" viewBox="0 0 470 110" preserveAspectRatio="none" aria-hidden="true">
      <defs>
        <linearGradient id="band" x1="0" x2="1" y1="0" y2="0">
          <stop offset="0" stop-color="#18324a"/>
          <stop offset=".5" stop-color="#2f5878"/>
          <stop offset="1" stop-color="#18324a"/>
        </linearGradient>
      </defs>
      <path d="M0 0 H470 V62 H90 Q40 62 20 90 L0 110 Z" fill="url(#band)"/>
    </svg>
    <div class="letterhead__mark">
      <span class="mark-square"></span><span>RIBEIRO TAVARES</span>
    </div>
    <div class="letterhead__watermark"></div>
    <footer class="letterhead__footer">
      <div class="brand-row"><span class="mark-square"></span><span class="brand-name">Ribeiro Tavares</span></div>
      <div class="brand-sub">ADVOGADOS E CONSULTORES</div>
      <div class="contact-row">
        <div class="contact-item"><span class="contact-icon"></span><span>(11) 3200-4100</span></div>
        <div class="contact-item"><span class="contact-icon"></span><span>Rua das Acácias, 120<br>São Paulo – SP</span></div>
        <div class="contact-item"><span class="contact-icon"></span><span>contato@ribeirotavares.adv.br</span></div>
        <div class="contact-item"><span class="contact-icon"></span><span>www.ribeirotavares.adv.br</span></div>
      </div>
    </footer>
  </section>

  <section class="folder">
    <div class="folder__brand">
      <div class="brand-row"><span class="mark-square"></span><span class="brand-name">Ribeiro Tavares</span></div>
      <div class="brand-sub">ADVOGADOS E CONSULTORES</div>
    </div>
    <div class="folder__watermark"></div>
    <div class="folder__stripe"></div>
  </section>
</body>
</html>
```